Ticket Website Design

The project is to design a website for a ticket business. We sell ticket for sports, theater and concerts.

- Below are some ticket design styles that we like -

PassHarbor.com
BrightRowz.com
GateNook.com
AdmitPlacing.com
Plov.com
FlenTrek.com

- Homepage features -

The main navigation should be the following links:
Upcoming, Sports, Concerts, Theater, Las Vegas, Location, Other

The main navigation should have a drop down menu designed.

The homepage should have a featured search box that is in a location that can be carried through to an internal page.

The site should be around 1000px width

We don't have a logo yet so you can use a placeholder in the logo location. I'll work to upload a placeholder logo if a designer don't have one.

We’d like to keep the background of the site lighter and not a dark solid background

You are free to do colors to your liking. However, please make them good combination colors and nothing that is very bright (i.e. Lime green). Some possible example colors would be “black/red”, “blue/orange”

We'd like the logo in the top left of the site.

- Other homepage elements -

Featured Events (Slider Box with Image)
Events In the Next 60 Days (Listing)
Newsletter (Form)
Buyer Guarantee (Design Box)
Testimonials (2 Featured Testimonials)
Featured Sports Tickets (Heading/Listing)
Featured Concert Tickets (Heading/Listing)
Featured Theater Tickets (Heading/Listing)
Featured Tickets By City (Heading/Listing)
Featured Phone Number / Less Featured International Number
Social Icons
“Your Location” See PassHarbor.com in the header. This shows the location of the visitor and features events in their area. They can click a small button to edit that location.

- What we are looking for overall -

We are looking for a high quality professional homepage design that contains all of the homepage features listed. While you are designing the homepage, please keep in mind the transition to an internal page. We want it to be a smooth transition. For example: if there is a column on the homepage, that column follows through on the internal page.

If you have some thoughts or questions on that let me know and I’d be happy to answer before you design.
Updates

Project Deadline Extended
Reason: A few designers asked for a few more days to submit their designs. Thanks for understanding. Let me know if anyone has any questions. Thanks, Dorn

Target Market(s)

18-35

Industry/Entity Type

Events

Requirements
Should not have
• No really bright colors (lime green/pink, etc.)

```html
<!DOCTYPE html>
<html lang="en">
<head>
<meta charset="utf-8">
<title>SeatLoom – Tickets for Sports, Concerts and Theater</title>
<link rel="stylesheet" href="https://fonts.googleapis.com/css2?family=Arimo:wght@400;700&display=swap">
<style>
:root{
  --red:#b3121b;
  --red-dark:#8d0b11;
  --red-deep:#6e080c;
  --ink:#222;
  --line:#d6d6d6;
  --panel:#fff;
  --page:#f4f4f4;
  --stripe:#ececec;
  --hero-top:#b5101a;
  --hero-bottom:#050505;
}
*{box-sizing:border-box;margin:0;padding:0}
html,body{width:751px;height:1200px;overflow:hidden}
body{position:relative;background:var(--page);font-family:"Arimo",Arial,sans-serif;color:var(--ink);font-size:9.5px}
a{color:inherit;text-decoration:none}
.abs{position:absolute}

/* header */
.site-header{left:0;top:0;width:751px;height:80px;background:#fff}
.brand{left:40px;top:24px;font-size:40px;font-weight:700;color:var(--red-dark);letter-spacing:-.5px;line-height:1}
.top-links{left:414px;top:28px;display:flex;gap:14px;font-size:10px;color:#333}
.location-box{left:439px;top:52px;width:113px;height:21px;border:1px solid #888;font-size:9.5px;padding:4px 8px;color:#222;background:#fff}
.phone{right:24px;top:22px;font-size:12.5px;color:#222;display:flex;align-items:center;gap:5px}
.phone-intl{right:24px;top:40px;font-size:9.5px;color:#333}
.social{right:23px;top:57px;display:flex;gap:4px}
.social span{width:15px;height:15px;border-radius:2px;background:#4a6ea8}
.social span:nth-child(1){background:#c8c8c8}
.social span:nth-child(4){background:#e0782b}
.social span:nth-child(5){background:#3f8a3a}

/* nav */
.main-nav{left:0;top:80px;width:751px;height:40px;background:linear-gradient(#c4161f,var(--red-dark));display:flex}
.main-nav a{height:40px;display:flex;align-items:center;justify-content:center;color:#fff;font-size:11.5px;border-right:1px solid rgba(0,0,0,.25);box-shadow:inset -1px 0 rgba(255,255,255,.15);position:relative}
.main-nav a:last-child{border-right:0;box-shadow:none}
.main-nav a.is-active{background:linear-gradient(#d9373c,#a4121a)}
.main-nav a.is-home::after{content:"";position:absolute;bottom:-1px;left:50%;margin-left:-4px;border:4px solid transparent;border-bottom-color:#fff}

/* hero */
.hero{left:0;top:120px;width:751px;height:195px;background:linear-gradient(var(--hero-top) 0%,#8a0a10 45%,var(--hero-bottom) 85%)}
.hero-title{right:15px;top:133px;color:#fff;font-size:22px;font-weight:400;text-shadow:0 1px 2px rgba(0,0,0,.6)}
.hero-search{left:557px;top:278px;width:171px;height:25px;background:#fff;border:1px solid #aaa;border-radius:3px;display:flex;align-items:center;font-size:8.5px;color:#666;padding-left:8px}
.hero-search .btn{position:absolute;right:0;top:0;width:24px;height:23px;border-left:1px solid #bbb;background:#eee;display:flex;align-items:center;justify-content:center}

.dropdown{left:187px;top:120px;width:87px;padding:2px 0 4px;background:var(--red-dark);box-shadow:0 2px 4px rgba(0,0,0,.4);z-index:5}
.dropdown a{display:block;height:22.5px;line-height:22.5px;padding-left:9px;color:#fff;font-size:9.5px;border-bottom:1px solid rgba(255,255,255,.2)}
.dropdown a:last-child{border-bottom:0}

/* panels */
.panel{background:var(--panel);border:1px solid #bfbfbf}
.panel-title{height:29px;line-height:29px;background:linear-gradient(#c3151e,var(--red-dark));color:#fff;font-size:12px;padding-left:12px}

.feature-tickets{left:21px;top:323px;width:169px;height:683px}
.feature-tickets ul{list-style:none}
.feature-tickets li{height:22.5px;line-height:22.5px;padding-left:14px;border-bottom:1px solid var(--line);font-size:9.5px;color:#222}
.feature-tickets li.group{color:var(--red);font-size:10px}

.slider{left:198px;top:323px;width:355px;height:157px}
.slide{position:absolute;top:8px;width:94px;height:141px}
.slider-arrow{position:absolute;top:75px;width:13px;height:13px;border-radius:50%;border:1px solid #999;background:#eee}

.events-60{left:198px;top:490px;width:355px;height:220px}
.events-60 table{width:100%;border-collapse:collapse;font-size:9px;table-layout:fixed}
.events-60 th{text-align:left;color:var(--red);font-weight:400;font-size:10px;height:22px;padding-left:12px;border-bottom:1px solid var(--line)}
.events-60 td{height:32px;padding-left:12px;vertical-align:middle;line-height:1.3;white-space:nowrap}
.events-60 td.act{padding-left:0}
.events-60 tr:nth-child(odd) td{background:var(--stripe)}
.ticket-btn{display:inline-block;background:var(--red);color:#fff;font-size:6.5px;padding:3px 5px;border-radius:1px}

.top-events{left:198px;top:712px;width:355px;height:408px}
.cat-head{display:flex;justify-content:space-between;padding:0 12px;height:24px;line-height:24px;font-size:10px;border-bottom:1px solid var(--line)}
.cat-head b{color:var(--red);font-weight:400}
.cat-row{display:flex;gap:13px;padding:5px 0 0 6px;height:102px;border-bottom:1px solid var(--line)}
.cat-row:last-child{border-bottom:0}
.cat-item{width:104px;text-align:center;font-size:9.5px}
.cat-item .pic{height:71px;margin-bottom:7px}

.newsletter{left:558px;top:323px;width:172px;height:137px}
.newsletter p{padding:11px 12px 0;line-height:1.45;font-size:9px}
.newsletter .field{margin:8px 12px 0;height:24px;border:1px solid #999;font-size:8.5px;color:#777;padding:6px 8px}
.newsletter .sub{display:block;padding:8px 12px;color:var(--red);font-size:9.5px}

.guarantee{left:558px;top:463px;width:172px;height:182px}
.guarantee p{padding:0 12px;font-size:9px;line-height:1.4}

.testimonials{left:558px;top:648px;width:172px;height:207px}
.quote{padding:11px 10px 0 12px;font-size:8.8px;line-height:1.45}
.quote cite{display:block;text-align:right;color:var(--red);font-style:italic;margin-top:3px}

/* footer */
.site-footer{left:0;top:1125px;width:751px;height:75px;background:var(--red-deep)}
.foot-nav{left:138px;top:1138px;display:flex;gap:22px;color:#fff;font-size:8.5px}
.foot-links{left:307px;top:1158px;display:flex;gap:20px;color:#fff;font-size:9.5px}
.copyright{left:333px;top:1177px;color:#fff;font-size:9px}
.foot-brand{left:642px;top:1138px;color:#fff;font-size:20px;font-weight:700}
.foot-social{left:598px;top:1172px;display:flex;gap:4px}
.foot-social span{width:14px;height:14px;border-radius:2px;background:#4a6ea8}
.foot-social span:nth-child(1){background:#ddd}
.foot-social span:nth-child(4){background:#e0782b}
.foot-social span:nth-child(5){background:#3f8a3a}
</style>
</head>
<body>

<header class="abs site-header">
  <div class="abs brand">SeatLoom</div>
  <nav class="abs top-links"><a href="#">About Us</a><a href="#">Contact Us</a><a href="#">Help</a></nav>
  <div class="abs location-box">Enter Location</div>
  <div class="abs phone">
    <svg width="11" height="11" viewBox="0 0 24 24" aria-hidden="true"><path fill="#222" d="M6.6 10.8a15 15 0 0 0 6.6 6.6l2.2-2.2c.3-.3.7-.4 1-.2 1.1.4 2.3.6 3.6.6.6 0 1 .4 1 1V20c0 .6-.4 1-1 1A17 17 0 0 1 3 4c0-.6.4-1 1-1h3.5c.6 0 1 .4 1 1 0 1.3.2 2.5.6 3.6.1.3 0 .7-.2 1z"/></svg>
    123 - 123 - 1234
  </div>
  <div class="abs phone-intl">View International Phone Number</div>
  <div class="abs social" aria-label="Share and follow links"><span></span><span></span><span></span><span></span><span></span></div>
</header>

<nav class="abs main-nav">
  <a href="#" class="is-home" style="width:104px">HOME</a>
  <a href="#" style="width:83px">UP COMING</a>
  <a href="#" class="is-active" style="width:87px">SPORTS</a>
  <a href="#" style="width:94px">CONCERT</a>
  <a href="#" style="width:91px">THEATER</a>
  <a href="#" style="width:91px">LAS VEGAS</a>
  <a href="#" style="width:121px">LOCATIONS</a>
  <a href="#" style="width:80px">OTHER</a>
</nav>

<section class="abs hero" role="img" aria-label="Red stage curtains with an audience in silhouette"></section>
<h1 class="abs hero-title">Interesting the event, get the seat now</h1>
<div class="abs hero-search">Search for Event, Artist, or Team
  <span class="btn"><svg width="11" height="11" viewBox="0 0 12 12" aria-hidden="true"><circle cx="5" cy="5" r="3.6" fill="none" stroke="#4a6ea8" stroke-width="1.6"/><path d="M7.6 7.6 11 11" stroke="#4a6ea8" stroke-width="1.8"/></svg></span>
</div>

<div class="abs dropdown">
  <a href="#">Football</a><a href="#">Basketball</a><a href="#">Hockey</a><a href="#">Baseball</a><a href="#">Racing</a><a href="#">Tennis</a>
</div>

<aside class="abs panel feature-tickets">
  <div class="panel-title">FEATURE TICKETS</div>
  <ul>
    <li class="group">SPORT TICKETS</li>
    <li>Harbor City Strikers</li><li>Bay Ridge Mariners</li><li>Coastal Gold Cup</li><li>2013 Pro League All-Star Game</li><li>Dallas Rangehands</li>
    <li class="group">CONCERT TICKETS</li>
    <li>Jordan Talbrook</li><li>Reyanna</li><li>Julian Brevard</li><li>Tessa Swale</li><li>Belinne</li>
    <li class="group">THEATER TICKETS</li>
    <li>Shore Boys</li><li>Wildwind</li><li>The Tiger Crown</li><li>Marigold - The Musical</li><li>The Book Of Marvin</li>
    <li class="group">TICKETS BY CITY</li>
    <li>Atlanta</li><li>Boston</li><li>Chicago</li><li>Dallas</li><li>Los Angeles</li><li>New York</li><li>Miami</li><li>Las Vegas</li><li>Indianapolis</li><li style="border-bottom:0">All Cities</li>
  </ul>
</aside>

<section class="abs panel slider">
  <span class="slider-arrow" style="left:6px"></span>
  <div class="slide" role="img" aria-label="Ballroom dance couple on stage" style="left:25px;background:linear-gradient(#6a1a14,#2a0d0a)"></div>
  <div class="slide" role="img" aria-label="Basketball player on court" style="left:129px;background:linear-gradient(#2b2b2b,#5a4a3a)"></div>
  <div class="slide" role="img" aria-label="Grand theatre auditorium" style="left:233px;background:linear-gradient(#c89a4a,#6a2a1a)"></div>
  <span class="slider-arrow" style="right:6px"></span>
</section>

<section class="abs panel events-60">
  <div class="panel-title">EVENTS IN THE NEXT 60 DAYS</div>
  <table>
    <tr><th style="width:110px">EVENTS</th><th style="width:82px">TIME</th><th style="width:118px">VENUE</th><th></th></tr>
    <tr><td>The Harmonic Parade</td><td>Jul 10, 2013<br>Wed, 5:30 PM</td><td>Bowen Ballroom<br>New York</td><td class="act"><span class="ticket-btn">TICKETS</span></td></tr>
    <tr><td>Ryan Calvera</td><td>Jul 10, 2013<br>Wed, 5:30 PM</td><td>Mainstreet Night Club<br>Allentown, PA</td><td class="act"><span class="ticket-btn">TICKETS</span></td></tr>
    <tr><td>The Book Of Marvin</td><td>Jul 10, 2013<br>Wed, 5:30 PM</td><td>Evelyn Ormond Theatre<br>New York, NY</td><td class="act"><span class="ticket-btn">TICKETS</span></td></tr>
    <tr><td>Marigold - The Musical</td><td>Jul 10, 2013<br>Wed, 5:30 PM</td><td>Shelby Theatre<br>New York, NY</td><td class="act"><span class="ticket-btn">TICKETS</span></td></tr>
    <tr><td>PRO ALL STAR GAME</td><td>Jul 10, 2013<br>Wed, 5:30 PM</td><td>Civic Field, New York</td><td class="act"><span class="ticket-btn">TICKETS</span></td></tr>
  </table>
</section>

<section class="abs panel top-events">
  <div class="panel-title">TOP EVENTS</div>
  <div class="cat-head"><b>SPORT EVENTS</b><a href="#">View All Events</a></div>
  <div class="cat-row">
    <div class="cat-item"><div class="pic" role="img" aria-label="Basketball and referee" style="background:linear-gradient(135deg,#c0692a,#2a2a2a)"></div>Basketball ticket</div>
    <div class="cat-item"><div class="pic" role="img" aria-label="Football players on a grass field" style="background:linear-gradient(#7a8a6a,#4a7a2a)"></div>American Football ticket</div>
    <div class="cat-item"><div class="pic" role="img" aria-label="Baseball batter at the plate" style="background:linear-gradient(#3a6a3a,#9a8a6a)"></div>Baseball ticket</div>
  </div>
  <div class="cat-head"><b>MUSIC EVENTS</b><a href="#">View All Events</a></div>
  <div class="cat-row">
    <div class="cat-item"><div class="pic" role="img" aria-label="Guitarist on a red-lit stage" style="background:linear-gradient(135deg,#8a1a0a,#e07a2a)"></div>Rock Music tickets</div>
    <div class="cat-item"><div class="pic" role="img" aria-label="Classical string players" style="background:linear-gradient(#1a1a1a,#5a2a1a)"></div>Clasic Music tickets</div>
    <div class="cat-item"><div class="pic" role="img" aria-label="Saxophone close-up" style="background:linear-gradient(135deg,#3a2a1a,#c8962a)"></div>Jazz Music tickets</div>
  </div>
  <div class="cat-head"><b>THEATER EVENTS</b><a href="#">View All Events</a></div>
  <div class="cat-row">
    <div class="cat-item"><div class="pic" role="img" aria-label="Costumed opera performer" style="background:linear-gradient(#2a3a5a,#a8782a)"></div>Clasic Opera tickets</div>
    <div class="cat-item"><div class="pic" role="img" aria-label="Ballet dancers on stage" style="background:linear-gradient(#1a1a2a,#8a8a9a)"></div>Ballet tickets</div>
    <div class="cat-item"><div class="pic" role="img" aria-label="Dancers under stage lights" style="background:linear-gradient(#0a0a0a,#5a5a6a)"></div>Dancing tickets</div>
  </div>
</section>

<aside class="abs panel newsletter">
  <div class="panel-title">NEWSLETTER</div>
  <p>Sign up for free update, discounts and events in your area</p>
  <div class="field">Enter email address</div>
  <a href="#" class="sub">Subscribe now</a>
</aside>

<aside class="abs panel guarantee">
  <div class="panel-title">BUYER GUARANTEE</div>
  <svg width="170" height="88" viewBox="0 0 170 88" aria-hidden="true"><circle cx="85" cy="45" r="35" fill="#c8131c"/></svg>
  <p>SeatLoom committed to provide you the best buying experience and a 100% Buyer Guarantee. Shop with confidence at SeatLoom</p>
</aside>

<aside class="abs panel testimonials">
  <div class="panel-title">TESTIMONIALS</div>
  <div class="quote">Thank you, I got my baseball tickets much cheaper than the other ticket sites. They were prompt on delivery I'm impressed!<cite>Effie Farano, New York</cite></div>
  <div class="quote">Thank you, I got my baseball tickets much cheaper than the other ticket sites. They were prompt on delivery I'm impressed!<cite>Effie Farano, New York</cite></div>
</aside>

<footer class="abs site-footer"></footer>
<nav class="abs foot-nav"><a href="#">HOME</a><a href="#">UP COMING</a><a href="#">SPORTS</a><a href="#">CONCERT</a><a href="#">THEATER</a><a href="#">LAS VEGAS</a><a href="#">LOCATIONS</a><a href="#">OTHER</a></nav>
<nav class="abs foot-links"><a href="#">About Us</a><a href="#">Contact Us</a><a href="#">Help</a></nav>
<div class="abs copyright">Copyright 2013 SeatLoom</div>
<div class="abs foot-brand">SeatLoom</div>
<div class="abs foot-social" aria-label="Share and follow links"><span></span><span></span><span></span><span></span><span></span></div>

</body>
</html>
```